依頼概要
■依頼の目的/概要
当方、鍼灸サロン店を運営しております。
メニューのデザインも新しいものに一新しようと考えております。

■要望ポイント
高級感のあれイメージでありつつもカフェや美容クリニックのような美的でおしゃれなデザインを希望致します。女性の方が多く利用されています。
古風なものは好ましくないです。

また新たに出張施術のサービスも、開始するためそのメニュー表の作成もお願いします。

■その他注意点など
店内の写真等HP、予約サイトもお送り致しますので、ある程度統一感のあるデザインにして頂きたいです。

その他何かご不明な点がございましたら、お気軽にご質問下さい。
よろしくお願いいたします。
メニュー表で出張施術を90分20000円〜交通費要相談
を新たに1ページ追加してほしいです。
■ 選んだ理由

デザインが良かったです。

■ 提案者全員のお礼・コメント

ありがとうございました。

```html
<!DOCTYPE html>
<html lang="ja">
<head>
<meta charset="UTF-8">
<title>施術メニュー</title>
<link rel="stylesheet" href="https://fonts.googleapis.com/css2?family=Playfair+Display:wght@900&family=Noto+Serif+JP:wght@500&family=Noto+Sans+JP:wght@400&display=swap">
<style>
  :root {
    --maroon: #5b1518;
    --maroon-line: #9a5a5c;
    --paper: #ffffff;
    --ink: #333333;
    --ink-soft: #555555;
    --rule-light: #e9e1e1;
  }
  * { margin: 0; padding: 0; box-sizing: border-box; }
  html, body { width: 848px; height: 1200px; overflow: hidden; background: var(--maroon); }
  .menu-sheet { position: relative; width: 848px; height: 1200px; background: var(--maroon); }
  .edge-line { position: absolute; top: 0; width: 1px; height: 1200px; background: var(--maroon-line); }
  .edge-line--left { left: 22px; }
  .edge-line--panel { left: 312px; }
  .edge-line--right { left: 800px; }
  .title-block { position: absolute; left: 72px; top: 204px; width: 156px; text-align: center; }
  .title-rule { height: 7px; border-top: 2px solid var(--maroon-line); border-bottom: 1px solid var(--maroon-line); }
  .title-text {
    font-family: "Playfair Display", serif; font-weight: 900; color: var(--paper);
    font-size: 48px; letter-spacing: 2px; line-height: 1; padding: 36px 0 38px;
  }
  .content-panel { position: absolute; left: 320px; top: 0; width: 438px; height: 1200px; background: var(--paper); }
  .menu-section { position: absolute; left: 90px; width: 260px; }
  .section-title {
    font-family: "Noto Serif JP", serif; font-weight: 500; font-size: 15px; color: var(--ink);
    text-align: center; letter-spacing: 3px; margin-bottom: 14px;
  }
  .price-list { list-style: none; }
  .price-row {
    display: flex; justify-content: space-between; height: 20px; align-items: center;
    font-family: "Noto Sans JP", sans-serif; font-size: 8.5px; color: var(--ink-soft);
    border-bottom: 1px solid var(--rule-light);
  }
  .section-note {
    margin-top: 18px; font-family: "Noto Sans JP", sans-serif; font-size: 7.5px; line-height: 16px;
    color: var(--ink-soft); text-align: center;
  }
</style>
</head>
<body>
<div class="menu-sheet">
  <div class="edge-line edge-line--left"></div>
  <div class="edge-line edge-line--panel"></div>

  <div class="title-block">
    <div class="title-rule"></div>
    <div class="title-text">MENU</div>
    <div class="title-rule"></div>
  </div>

  <main class="content-panel">
    <section class="menu-section" style="top:306px">
      <h2 class="section-title">鍼灸</h2>
      <ul class="price-list">
        <li class="price-row"><span>【初回の方】鍼灸施術 30分</span><span>7,600円</span></li>
        <li class="price-row"><span>【初回の方】鍼灸施術 90分</span><span>9,800円</span></li>
        <li class="price-row"><span>【初回の方】鍼灸施術 120分</span><span>12,000円</span></li>
        <li class="price-row"><span>【2回目以降の方】鍼灸施術60分</span><span>6,800円</span></li>
        <li class="price-row"><span>【2回目以降の方】鍼灸施術 90分</span><span>8,800円</span></li>
        <li class="price-row"><span>【2回目以降の方】鍼灸施術 120分</span><span>11,000円</span></li>
        <li class="price-row"><span>オプションメニュー延長15分</span><span>2,200円</span></li>
      </ul>
      <p class="section-note">※初回の方は施術前に、カウンセリング料（1,000円）が加算されます。<br>※表示価格はすべて税込価格です。</p>
    </section>

    <section class="menu-section" style="top:620px">
      <h2 class="section-title">美容鍼</h2>
      <ul class="price-list">
        <li class="price-row"><span>【初回の方】美容鍼 30分</span><span>5,400円</span></li>
        <li class="price-row"><span>【2回目以降の方】美容鍼 30分</span><span>4,400円</span></li>
        <li class="price-row"><span>オプションメニュー延長15分</span><span>2,200円</span></li>
      </ul>
      <p class="section-note">※初回の方は施術前に、カウンセリング料（1,000円）が加算されます。<br>※表示価格はすべて税込価格です。</p>
    </section>

    <section class="menu-section" style="top:860px">
      <h2 class="section-title">水素灸</h2>
      <ul class="price-list">
        <li class="price-row"><span>【初回の方】水素温灸美容鍼 30分</span><span>6,900円</span></li>
        <li class="price-row"><span>【2回目以降の方】水素温灸美容鍼 30分</span><span>5,900円</span></li>
        <li class="price-row"><span>オプションメニュー延長15分</span><span>2,200円</span></li>
      </ul>
      <p class="section-note">※初回の方は施術前に、カウンセリング料（1,000円）が加算されます。<br>※水素温灸を追加の場合は、1部位につき1,000円です。<br>※オプションは当日も承ります。<br>※表示価格はすべて税込価格です。</p>
    </section>
  </main>

  <div class="edge-line edge-line--right"></div>
</div>
</body>
</html>
```